Software as a Service to manage Home Care Management

We need a web site designed for Home Care Management Software as a Service product, that facilitates Home Care organizations to manage and schedule carers to visit client homes. We want a modern look and feel using our existing logo.

Target Market(s)

Home Care Management organizations. Product is similar to: https://wovenpath.co/

Coding

Coded - Design and coding required

Number of Pages Required

3 page

```html
<!DOCTYPE html>
<html lang="en">
<head>
<meta charset="utf-8">
<title>Tendwell – Home Care Management</title>
<link rel="stylesheet" href="https://fonts.googleapis.com/css2?family=Cinzel:wght@400;600&family=Mulish:wght@400;600;700&display=swap">
<style>
:root{
  --pink:#fb3d7e;
  --pink-deep:#d91f5d;
  --pink-soft:#fdeff4;
  --dark:#333132;
  --ink:#3a3a3a;
  --muted:#8a8a8a;
  --white:#ffffff;
  --head:'Cinzel',serif;
  --body:'Mulish',sans-serif;
}
*{box-sizing:border-box;margin:0;padding:0}
html,body{width:1200px;height:4996px;overflow:hidden}
body{position:relative;background:var(--white);font-family:var(--body);color:var(--ink)}
.abs{position:absolute}
.head{font-family:var(--head);font-weight:400;letter-spacing:1px}
.mark-line{position:absolute;height:2px;background:var(--pink)}
.mark-dot{position:absolute;width:22px;height:22px;border-radius:50%;border:3px solid var(--pink)}
.btn{position:absolute;display:flex;align-items:center;justify-content:center;border-radius:22px;font-family:var(--head);font-size:12px;font-weight:600;letter-spacing:.5px}
.btn-pink{background:var(--pink);color:var(--white)}
.btn-outline{border:2px solid var(--dark);color:var(--dark)}

/* header */
.site-header{position:absolute;top:0;left:0;width:1200px;height:78px;background:var(--white);z-index:5}
.brand{position:absolute;display:flex;align-items:center;gap:8px;font-family:var(--head);font-weight:600}
.brand-dot{width:22px;height:22px;border-radius:50%;background:var(--pink)}
.nav a{position:absolute;top:30px;font-family:var(--head);font-size:14px;color:var(--dark);text-decoration:none}
.nav a.active{color:var(--pink)}
.header-cta{position:absolute;right:0;top:0;width:262px;height:78px;background:var(--pink);color:var(--white);font-family:var(--head);font-size:16px;display:flex;align-items:center;justify-content:center;letter-spacing:1px}

/* hero */
.hero-photo{position:absolute;top:78px;left:0;width:1200px;height:610px;background:linear-gradient(100deg,#8e8f74 0%,#c9bfb3 30%,#ece9e5 55%,#f3f1ef 100%)}
.hero-title{left:726px;top:244px;font-size:46px;line-height:48px;color:var(--dark)}

/* about */
.about-circle{left:68px;top:706px;width:522px;height:522px;border-radius:50%;background:var(--pink-soft)}
.about-photo{left:112px;top:770px;width:470px;height:470px;border-radius:50%;background:radial-gradient(circle at 45% 40%,#d9c3b8,#9fb2c4 60%,#c8ccd0)}
.para{font-size:14.5px;line-height:24px;color:var(--muted)}

.features-list{list-style:none;left:172px;top:1585px}
.features-list li{display:flex;align-items:center;gap:10px;height:31px;font-size:15.5px;color:var(--dark)}
.tick{width:16px;height:16px;border-radius:50%;background:var(--pink);display:flex;align-items:center;justify-content:center}

/* phone */
.phone{left:697px;top:1339px;width:330px;height:678px;border-radius:44px;background:var(--white);border:2px solid #e2e2e2;box-shadow:0 8px 30px rgba(0,0,0,.15);z-index:3}
.screen{position:absolute;left:16px;top:72px;width:296px;height:528px;background:var(--pink)}
.screen-top{height:78px;background:var(--pink-deep);display:flex;align-items:center;justify-content:center;color:var(--white);font-family:var(--head);font-size:18px}
.date-bar{position:absolute;left:22px;top:94px;width:252px;height:48px;background:var(--pink-deep);color:var(--white);text-align:center;font-family:var(--head);font-size:12px;padding-top:8px;border-radius:3px}
.date-bar small{display:block;font-family:var(--body);font-size:10px}
.visit-card{position:absolute;left:22px;top:154px;width:252px;height:350px;background:var(--white);text-align:center}
.pill{position:absolute;left:56px;width:160px;height:40px;border-radius:20px;color:var(--white);font-family:var(--head);font-size:13px;display:flex;align-items:center;justify-content:center}

/* pink band */
.band-title{width:1200px;left:0;top:2106px;text-align:center;font-size:36px;color:var(--white)}
.role{position:absolute;top:2200px;width:250px;text-align:center;color:var(--white)}
.role-icon{width:128px;height:128px;margin:0 auto;border-radius:50%;background:var(--white);border:5px solid var(--pink);box-shadow:0 0 0 3px var(--white);display:flex;align-items:center;justify-content:center}
.role h3{font-family:var(--head);font-weight:400;font-size:17px;margin-top:22px;line-height:20px}
.role p{font-size:13px;line-height:17px;margin-top:6px}

.video{left:174px;top:2550px;width:852px;height:482px;background:var(--white);padding:8px;box-shadow:0 6px 20px rgba(0,0,0,.2)}
.video-fill{width:100%;height:100%;background:linear-gradient(100deg,#4d6d96 0%,#8c8f97 40%,#d7d0c4 60%,#3f87c9 85%)}

/* key features */
.card{position:absolute;top:3309px;width:219px;height:306px;border-radius:0 0 26px 0;background:var(--dark);overflow:hidden;text-align:center;color:#bdbdbd}
.card-top{height:126px;background:var(--pink);border-radius:26px 0 0 0;display:flex;align-items:center;justify-content:center}
.card h3{font-family:var(--head);font-weight:400;color:var(--white);font-size:21px;margin-top:24px}
.card p{font-size:14px;line-height:21px;margin:10px 24px 0}

/* contact */
.contact-title{left:172px;top:3976px;font-size:44px;line-height:54px;color:var(--white)}
.field{position:absolute;left:172px;width:323px;height:38px;border:1.5px solid rgba(255,255,255,.8);border-radius:19px;color:var(--white);font-size:12px;font-weight:700;padding:11px 14px}
.book{position:absolute;left:172px;top:4366px;width:323px;height:40px;border-radius:20px;background:var(--dark);color:var(--white);font-family:var(--head);font-size:17px;display:flex;align-items:center;justify-content:center;letter-spacing:1px}

/* footer */
.site-footer{position:absolute;left:0;top:4576px;width:1200px;height:420px;background:var(--dark);color:#cfcfcf}
.foot-col{position:absolute;top:140px;font-size:13.5px;line-height:25px}
.news{left:751px;top:130px;font-size:18px;color:#e0e0e0}
.news-input{left:751px;top:169px;width:275px;height:40px;border-radius:20px;background:var(--white);color:var(--dark);font-size:12px;padding:12px 16px}
.news-btn{position:absolute;right:4px;top:4px;width:82px;height:32px;border-radius:16px;background:var(--pink);color:var(--white);font-size:12px;font-weight:700;display:flex;align-items:center;justify-content:center}
.social{position:absolute;top:4922px;width:22px;height:22px;border-radius:50%;background:var(--pink)}
</style>
</head>
<body>

<header class="site-header">
  <div class="brand" style="left:56px;top:24px;font-size:19px;color:var(--dark)"><span class="brand-dot"></span>Tendwell</div>
  <nav class="nav">
    <a class="active" style="left:346px">Home</a>
    <a style="left:424px">Product</a>
    <a style="left:530px">Pricing</a>
    <a style="left:627px">Blog</a>
    <a style="left:705px">FAQ</a>
    <a style="left:772px">Contact Us</a>
  </nav>
  <div class="header-cta">Book a free demo</div>
</header>

<!-- hero -->
<section>
  <div class="hero-photo" role="img" aria-label="Young carer helping an elderly woman use a smartphone at home"></div>
  <div class="mark-line" style="left:726px;top:226px;width:130px"></div>
  <div class="mark-dot" style="left:856px;top:214px"></div>
  <h1 class="abs head hero-title">Care Software<br>for the Heroes<br>of Homecare</h1>
  <div class="btn btn-pink" style="left:726px;top:418px;width:188px;height:44px">See how it works</div>
  <svg class="abs" style="left:0;top:600px" width="1200" height="100" viewBox="0 0 1200 100">
    <path d="M0 66 C280 120 620 10 1200 22 L1200 66 C760 44 420 118 0 96Z" fill="var(--pink)"/>
    <path d="M0 86 C380 128 720 52 1200 60 L1200 100 L0 100Z" fill="#fff"/>
  </svg>
</section>

<!-- about -->
<section>
  <div class="abs about-circle"></div>
  <div class="abs about-photo" role="img" aria-label="Collage of carers with elderly clients"></div>
  <div class="abs" style="left:1006px;top:1074px;width:300px;height:300px;border-radius:50%;background:var(--pink-soft)"></div>
  <div class="mark-line" style="left:629px;top:794px;width:130px"></div>
  <div class="mark-dot" style="left:759px;top:782px"></div>
  <h2 class="abs head" style="left:629px;top:806px;font-size:38px;color:var(--dark)">About Us</h2>
  <p class="abs para" style="left:629px;top:861px;width:400px">Lorem ipsum dolor sit amet, consectetur adipiscing eit, sed do eiusmod tempor incididunt ut labore et dolora na aliquat enim ad minim veniam, quis nostrorem ipsu mdolor sit amet, consectetur adipiscing eit, ed do eius mod tempor incididunt ut labore et doloraa aliquat en imd minim veniam, quis nostr.od tempor incididunt ut labore et doloraa aliquat enim ad minim veniam, quis nostrorem ipsu mdolor sit amet, consectetur adipiscing eit, ed do eius mod tempor incididunt ut labore eloremt doloraa aliquat en imd minim veniam.</p>
  <div class="btn btn-outline" style="left:629px;top:1122px;width:132px;height:40px">Read more</div>
</section>

<!-- optimised -->
<section>
  <div class="mark-line" style="left:172px;top:1382px;width:130px"></div>
  <div class="mark-dot" style="left:302px;top:1370px"></div>
  <h2 class="abs head" style="left:172px;top:1388px;font-size:38px;line-height:42px;color:var(--dark)">Optimised Home<br>Care Software</h2>
  <p class="abs para" style="left:172px;top:1488px;width:410px">Lorem ipsum dolor sit amet, consectetur adipiscing eit, sed do eiusmod tempor incididunt ut labore et dolora na aliquat enim ad minim veniam, quis nostr.</p>
  <ul class="abs features-list">
    <li><span class="tick"><svg width="10" height="10" viewBox="0 0 10 10"><path d="M2 5l2 2 4-4" stroke="#fff" stroke-width="1.8" fill="none"/></svg></span>All-in-one home care software</li>
    <li><span class="tick"><svg width="10" height="10" viewBox="0 0 10 10"><path d="M2 5l2 2 4-4" stroke="#fff" stroke-width="1.8" fill="none"/></svg></span>Create staff rotas with automated scheduling tools</li>
    <li><span class="tick"><svg width="10" height="10" viewBox="0 0 10 10"><path d="M2 5l2 2 4-4" stroke="#fff" stroke-width="1.8" fill="none"/></svg></span>Tailored care plans &amp; risk assessments for your clients</li>
    <li><span class="tick"><svg width="10" height="10" viewBox="0 0 10 10"><path d="M2 5l2 2 4-4" stroke="#fff" stroke-width="1.8" fill="none"/></svg></span>Check in/out from a client visit using the app</li>
    <li><span class="tick"><svg width="10" height="10" viewBox="0 0 10 10"><path d="M2 5l2 2 4-4" stroke="#fff" stroke-width="1.8" fill="none"/></svg></span>Reporting suite for payroll, invoices, inspections &amp; more!</li>
    <li><span class="tick"><svg width="10" height="10" viewBox="0 0 10 10"><path d="M2 5l2 2 4-4" stroke="#fff" stroke-width="1.8" fill="none"/></svg></span>Easy to set up and use. Get started today!</li>
  </ul>
  <div class="btn btn-pink" style="left:172px;top:1807px;width:178px;height:42px">Book a free demo</div>
  <div class="btn btn-outline" style="left:360px;top:1807px;width:132px;height:42px">Read more</div>

  <div class="abs phone">
    <div class="abs" style="left:135px;top:38px;width:56px;height:4px;border-radius:2px;background:#bbb"></div>
    <div class="screen">
      <div class="screen-top">Tendwell</div>
      <div class="date-bar">
        <svg class="abs" style="left:10px;top:16px" width="10" height="14"><path d="M8 1L2 7l6 6" stroke="#fff" stroke-width="2.5" fill="none"/></svg>
        Sun Dec 06<small>08:00 - 1:00</small>
        <svg class="abs" style="right:10px;top:16px" width="10" height="14"><path d="M2 1l6 6-6 6" stroke="#fff" stroke-width="2.5" fill="none"/></svg>
      </div>
      <div class="visit-card">
        <div class="abs" style="left:14px;top:14px;width:44px;height:44px;border-radius:50%;background:#c9ccd2"></div>
        <div class="abs" style="left:68px;top:18px;text-align:left;font-size:13px;line-height:16px;color:var(--dark);font-weight:600">Dana Price<br><span style="font-weight:400">Lorem suos</span></div>
        <svg class="abs" style="right:12px;top:26px" width="10" height="14"><path d="M2 1l6 6-6 6" stroke="#333" stroke-width="2.5" fill="none"/></svg>
        <p class="abs" style="left:28px;top:94px;width:196px;font-size:13.5px;line-height:23px;color:var(--muted)">Lorem ipsum dolor sit amet, consectetur adipiscing eit, sed do eiusmod tempor in</p>
        <div class="pill" style="top:210px;background:var(--pink)">+Create Visit</div>
        <div class="pill" style="top:264px;background:var(--dark)">+Create Event</div>
      </div>
    </div>
    <div class="abs" style="left:136px;top:612px;width:52px;height:52px;border-radius:50%;border:2px solid #ddd"></div>
  </div>
</section>

<!-- pink band -->
<section>
  <svg class="abs" style="left:0;top:1950px" width="1200" height="890" viewBox="0 0 1200 890">
    <path d="M0 22 C260 70 560 40 760 20 L760 60 C520 60 260 90 0 60Z" fill="var(--dark)"/>
    <path d="M0 52 C300 82 560 58 800 40 L1200 40 L1200 885 L0 885Z" fill="var(--pink)"/>
  </svg>
  <div class="mark-line" style="left:534px;top:2088px;width:130px;background:#fff"></div>
  <div class="mark-dot" style="left:664px;top:2076px;border-color:#fff"></div>
  <h2 class="abs head band-title">We have made Tendwell</h2>

  <div class="role" style="left:163px">
    <div class="role-icon"><svg width="48" height="52" viewBox="0 0 48 52"><circle cx="24" cy="15" r="11" stroke="#333" stroke-width="4" fill="none"/><path d="M4 50c0-12 9-20 20-20s20 8 20 20" stroke="#333" stroke-width="4" fill="none"/></svg></div>
    <h3>For Managers</h3>
    <p>Lorem ipsum dolor sit amet consectetur adipiscing elitsed do eiusmod tempor incididun laboorem isum dolors.</p>
  </div>
  <div class="role" style="left:473px">
    <div class="role-icon"><svg width="50" height="46" viewBox="0 0 50 46"><path d="M25 42L6 23C-1 15 4 4 14 4c5 0 9 3 11 7 2-4 6-7 11-7 10 0 15 11 8 19Z" stroke="#333" stroke-width="4" fill="none"/></svg></div>
    <h3>For Carers</h3>
    <p>Lorem ipsum dolor sit amet consectetur adipiscing elitsed do eiusmod tempor incididun laboorem isum dolors.</p>
  </div>
  <div class="role" style="left:780px">
    <div class="role-icon"><svg width="48" height="46" viewBox="0 0 48 46"><path d="M4 22L24 4l20 18M9 18v24h30V18M20 42V30h8v12" stroke="#333" stroke-width="4" fill="none" stroke-linejoin="round"/></svg></div>
    <h3>For Clients<br>and Families</h3>
    <p>Lorem ipsum dolor sit amet consectetur adipiscing elitsed do eiusmod temporcidun.</p>
  </div>

  <div class="abs video"><div class="video-fill" role="img" aria-label="Carer showing a phone to an elderly woman in her living room"></div></div>
  <div class="abs" style="left:552px;top:2746px;width:92px;height:92px;border-radius:50%;background:#2b2b2b;border:4px solid var(--pink)"></div>
  <svg class="abs" style="left:586px;top:2774px" width="30" height="36"><path d="M2 2l26 16-26 16Z" fill="#fff"/></svg>
</section>

<!-- key features -->
<section>
  <div class="mark-line" style="left:534px;top:3138px;width:130px"></div>
  <div class="mark-dot" style="left:664px;top:3126px"></div>
  <h2 class="abs head" style="left:0;width:1200px;top:3148px;text-align:center;font-size:34px;color:var(--dark)">Key Features</h2>
  <p class="abs para" style="left:330px;width:540px;top:3205px;text-align:center">Lorem ipsum dolor sit amet, consectetur adipiscing eit, sed do eiusmod tempor incididunt ut labore et dolorana aliquat enim ad minim.</p>

  <div class="card" style="left:236px">
    <div class="card-top"><svg width="50" height="50" viewBox="0 0 50 50"><rect x="4" y="8" width="42" height="38" rx="3" stroke="#fff" stroke-width="3" fill="none"/><path d="M4 18h42M14 3v10M36 3v10" stroke="#fff" stroke-width="3"/><g fill="#fff"><rect x="11" y="24" width="5" height="5"/><rect x="22" y="24" width="5" height="5"/><rect x="33" y="24" width="5" height="5"/><rect x="11" y="34" width="5" height="5"/><rect x="22" y="34" width="5" height="5"/></g></svg></div>
    <h3>Roster</h3>
    <p>Lorem ipsum dolor sit amet, consectetur adipiscing eit, sed do eiusmod tempor</p>
  </div>
  <div class="card" style="left:490px">
    <div class="card-top"><svg width="50" height="50" viewBox="0 0 50 50"><g fill="#fff"><rect x="4" y="34" width="7" height="14"/><rect x="15" y="26" width="7" height="22"/><rect x="26" y="30" width="7" height="18"/><rect x="37" y="18" width="7" height="30"/></g><path d="M4 24l12-10 10 6 16-14" stroke="#fff" stroke-width="3" fill="none"/></svg></div>
    <h3>Reports</h3>
    <p>Lorem ipsum dolor sit amet, consectetur adipiscing eit, sed do eiusmod tempor</p>
  </div>
  <div class="card" style="left:743px">
    <div class="card-top"><svg width="50" height="50" viewBox="0 0 50 50"><path d="M34 20V4H6v42h20" stroke="#fff" stroke-width="3" fill="none"/><path d="M12 12h16M12 20h16M12 28h10" stroke="#fff" stroke-width="3"/><circle cx="38" cy="32" r="6" stroke="#fff" stroke-width="3" fill="none"/><path d="M28 48c0-6 4-9 10-9s10 3 10 9" stroke="#fff" stroke-width="3" fill="none"/></svg></div>
    <h3>Care Plans</h3>
    <p>Lorem ipsum dolor sit amet, consectetur adipiscing eit, sed do eiusmod tempor</p>
  </div>
  <div class="abs" style="left:572px;top:3667px;display:flex;gap:5px">
    <span style="width:11px;height:11px;border-radius:50%;background:var(--dark)"></span><span style="width:11px;height:11px;border-radius:50%;background:var(--dark)"></span><span style="width:11px;height:11px;border-radius:50%;background:var(--dark)"></span><span style="width:11px;height:11px;border-radius:50%;background:var(--dark)"></span>
  </div>
</section>

<!-- contact -->
<section>
  <svg class="abs" style="left:0;top:3750px" width="1200" height="830" viewBox="0 0 1200 830">
    <path d="M0 40 C300 0 700 10 1200 22 L1200 56 C760 44 320 50 0 76Z" fill="var(--dark)"/>
    <path d="M0 70 C320 46 760 42 1200 50 L1200 830 L0 830Z" fill="var(--pink)"/>
  </svg>
  <div class="mark-line" style="left:172px;top:3962px;width:100px;background:#fff"></div>
  <div class="mark-dot" style="left:272px;top:3950px;border-color:#fff"></div>
  <h2 class="abs head contact-title">Want to<br>know more?</h2>
  <div class="field" style="top:4114px">Name</div>
  <div class="field" style="top:4164px">Company Name*</div>
  <div class="field" style="top:4216px">Phone Number*</div>
  <div class="field" style="top:4268px">Email*</div>
  <div class="field" style="top:4321px;width:158px">Demo date</div>
  <div class="field" style="top:4321px;left:337px;width:158px">Time
    <svg class="abs" style="right:14px;top:15px" width="10" height="6"><path d="M0 0h10L5 6Z" fill="#fff"/></svg></div>
  <div class="book">Book now</div>
  <div class="abs" style="left:687px;top:3947px;width:416px;height:426px;border-radius:50%;background:radial-gradient(circle,#f7d9e2,#f4a9c1 60%,rgba(251,61,126,0))" role="img" aria-label="Photo collage of carers and elderly clients"></div>
</section>

<footer class="site-footer">
  <div class="brand" style="left:172px;top:68px;font-size:19px;color:#e8e8e8"><span class="brand-dot"></span>Tendwell</div>
  <div class="foot-col" style="left:172px">App<br>Managers<br>Carers<br>Customers &amp; Family</div>
  <div class="foot-col" style="left:368px">About us<br>Contact us<br>Work with us</div>
  <div class="foot-col" style="left:526px">Get started<br>FAQ<br>Pricing</div>
  <div class="abs news">Get the latest news from us!</div>
  <div class="abs news-input">Email:<span class="news-btn">SIGN UP</span></div>
  <div class="abs" style="left:172px;top:267px;width:856px;height:1px;background:#555"></div>
  <div class="abs" style="left:0;width:1200px;top:292px;text-align:center;font-size:13px">© 2020 All rights reserved. Terms &amp; Privacy</div>
</footer>
<span class="social" style="left:513px"></span>
<span class="social" style="left:562px"></span>
<span class="social" style="left:608px"></span>
<span class="social" style="left:657px"></span>

</body>
</html>
```